Website for UK Fintech Company specialising in Auto-Finance asset management

We need a website for a FINTECH business called KELP Asset Management. We have developed and licenced an innovative platform to provide financial institutions whom provide secured Asset finance loans to consumer and commercial clients, allowing for real time tracking and management of defaulted accounts pending repossession. The KELP Asset Management platform is a total recoveries solution through the cycle, from the moment the lender has to recover the vehicle (due to default/non-payment) to the disposal of the vehicle (via sale at Motor Auctions or by selling to a Car dealership network). The data provided from external services allows the Financier to make informed decisions, such as whether it is economical to continue the recovery and decide which sales channel is better suited for their assets to maximise residual values and minimise financial losses. The KELP platform provides an array of MI reporting and uses a systematic approach utilising exception reporting to identify key areas of non-performance to enable focus where needed. KELP also provides a leading Debt collection service recovering end-of-cycle losses such as Financial Shortfall and losses in vehicle values due to conditions and excessive damage.

We also require a new logo for out new product called MB-Prismo

Target Market(s)

Financial institutions whom provide secured Asset finance loans to consumer and commercial clients

Industry/Entity Type

Financial Service

Logo Text

MB- Prismo (this is for a new product which forms part of the KELP Asset Mangement Platform

Number of Pages Required

4 page

Font styles to use
Serif
Sans Serif

Colors

Designer to choose colors to be used in the design.

Requirements
Must have
• We need a simple website with a broken down as follows;
• • Landing page
• • Services page
• • About us page
• • KELP Asset Management Platform login page (client facing)
Nice to have
• Our slogan is 'Auto-Finance Expertise'
• We are very much open to suggestions as long as we can create a professional/ corporate / modern feel to the website. We are a FINTECH company, and that needs to come across
Should not have
• Whilst we are an asset management company primarily managing vehicles through our platform, we don't want it to look like a car dealership website!:)

```html
<!DOCTYPE html>
<html lang="en">
<head>
<meta charset="utf-8">
<title>KELP Asset Management</title>
<link href="https://fonts.googleapis.com/css2?family=Raleway:wght@600;700;800&family=Open+Sans:wght@400;600&display=swap" rel="stylesheet">
<style>
:root{
  --orange:#d2691c;
  --dark:#1f1f1f;
  --ink:#2a2a2a;
  --body:#555;
  --white:#fff;
  --rule:#cfcfcf;
}
*{box-sizing:border-box;margin:0;padding:0}
html,body{width:895px;height:1200px;overflow:hidden;background:#fff}
body{position:relative;font-family:"Open Sans",sans-serif;color:var(--body)}
.hero{position:absolute;left:0;top:0;width:895px;height:408px;
  background:linear-gradient(135deg,#4a4a4a 0%,#6d6a66 35%,#3b3b3b 65%,#1e1e1e 100%)}
.brand{position:absolute;left:73px;top:24px;
  font-family:"Raleway",sans-serif;font-weight:800;font-size:40px;line-height:44px;color:var(--white);letter-spacing:1px}
.nav{position:absolute;top:37px;left:420px;font-family:"Raleway",sans-serif;font-weight:700;font-size:12.5px;color:var(--white)}
.nav a{color:inherit;text-decoration:none;position:absolute;white-space:nowrap}
.nav .active{color:var(--orange)}
.search{position:absolute;left:809px;top:38px}
.hero-title{position:absolute;top:122px;width:100%;text-align:center;font-family:"Raleway",sans-serif;font-weight:700;font-size:50px;color:var(--white)}
.hero-sub{position:absolute;top:190px;width:100%;text-align:center;font-size:18px;line-height:26px;color:var(--white)}
.hero-btn{position:absolute;left:385px;top:262px;width:126px;height:41px;border:2px solid var(--white);
  color:var(--white);font-family:"Raleway",sans-serif;font-weight:700;font-size:12.5px;display:flex;align-items:center;justify-content:center}
.arrow{position:absolute;top:184px;width:30px;height:40px;background:rgba(0,0,0,.35)}
.arrow.left{left:0}.arrow.right{right:0}
.features{position:absolute;top:355px;left:0;width:895px}
.feature{position:absolute;width:180px;text-align:center}
.feature .ring{width:104px;height:104px;margin:0 auto;border-radius:50%;background:#fff;border:3px solid var(--orange);display:flex;align-items:center;justify-content:center}
.feature .ring span{width:88px;height:88px;border-radius:50%;border:4px solid var(--orange);display:flex;align-items:center;justify-content:center}
.feature h3{margin-top:16px;font-family:"Raleway",sans-serif;font-weight:700;font-size:15px;color:var(--ink)}
.divider{position:absolute;left:73px;top:529px;width:749px;height:1px;background:var(--rule)}
.welcome h2{position:absolute;left:73px;top:576px;font-family:"Raleway",sans-serif;font-weight:700;font-size:22px;line-height:30px;color:var(--ink)}
.welcome p{position:absolute;left:73px;top:652px;width:420px;font-size:10.8px;line-height:21px;color:var(--body)}
.btn{position:absolute;left:73px;top:827px;width:108px;height:38px;background:var(--orange);color:#fff;
  font-family:"Raleway",sans-serif;font-weight:700;font-size:12.5px;display:flex;align-items:center;justify-content:center}
.screen{position:absolute;left:511px;top:583px;width:342px;height:277px;border-radius:8px;
  background:linear-gradient(180deg,#1a1a1a 0%,#e8e8ec 6%,#dcdde2 68%,#b8b8bd 78%,#9a9a9e 100%)}
.footer{position:absolute;left:0;top:931px;width:895px;height:269px;background:var(--dark);border-top:3px solid var(--orange);color:#fff}
.footer .brand{left:64px;top:66px;font-size:50px;line-height:54px}
.col{position:absolute;top:48px}
.col h4{font-family:"Raleway",sans-serif;font-weight:700;font-size:13.5px;margin-bottom:14px}
.links li{list-style:none;font-size:9.5px;line-height:17.2px}
.news p{font-size:9.5px;line-height:15px;width:200px}
.news .field{margin-top:10px;width:189px;height:26px;background:#fff;color:#333;font-size:9px;padding:7px 10px}
.news .sub{margin-top:9px;width:74px;height:27px;background:var(--orange);font-family:"Raleway",sans-serif;font-weight:700;font-size:9.5px;display:flex;align-items:center;justify-content:center}
.contact li{list-style:none;display:flex;gap:10px;font-size:9.5px;line-height:12.5px;margin-bottom:11px}
.contact svg{flex:none;margin-top:1px}
.bottom-rule{position:absolute;left:73px;top:211px;width:749px;height:1px;background:#3c3c3c}
.copy{position:absolute;left:73px;top:232px;font-size:9.5px}
.social{position:absolute;left:705px;top:226px;display:flex;gap:7px}
.social span{width:24px;height:24px;border-radius:50%;border:1.5px solid #fff}
</style>
</head>
<body>
<header class="hero" role="img" aria-label="Photo of hands working on a laptop and financial charts, dark overlay">
</header>
<div class="brand">KELP</div>
<nav class="nav">
  <a class="active" style="left:0">HOME</a>
  <a style="left:61px">ABOUT US</a>
  <a style="left:147px">SERVICES</a>
  <a style="left:230px">BLOG</a>
  <a style="left:289px">CONTACT US</a>
</nav>
<svg class="search" width="12" height="12" viewBox="0 0 12 12"><circle cx="5" cy="5" r="3.6" fill="none" stroke="#fff" stroke-width="1.8"/><line x1="7.6" y1="7.6" x2="11" y2="11" stroke="#fff" stroke-width="2"/></svg>
<h1 class="hero-title">KELP Asset Management</h1>
<p class="hero-sub">We are an asset management company primarily<br>managing vehicles through our platform</p>
<div class="hero-btn">GET MORE INFO</div>
<div class="arrow left"><svg width="30" height="40"><polyline points="18,13 11,20 18,27" fill="none" stroke="#fff" stroke-width="2"/></svg></div>
<div class="arrow right"><svg width="30" height="40"><polyline points="12,13 19,20 12,27" fill="none" stroke="#fff" stroke-width="2"/></svg></div>

<section class="features">
  <div class="feature" style="left:51px"><div class="ring"><span>
    <svg width="48" height="36" viewBox="0 0 48 36"><path d="M2 2V34H46" fill="none" stroke="#222" stroke-width="3"/><rect x="9" y="20" width="5" height="11" fill="#222"/><rect x="17" y="14" width="5" height="17" fill="#222"/><rect x="25" y="18" width="5" height="13" fill="#222"/><rect x="33" y="8" width="5" height="23" fill="#222"/></svg>
  </span></div><h3>Asset Management</h3></div>
  <div class="feature" style="left:256px"><div class="ring"><span>
    <svg width="30" height="36" viewBox="0 0 30 36"><path d="M8 16V10a7 7 0 0 1 14 0v6" fill="none" stroke="#222" stroke-width="4"/><rect x="1" y="15" width="28" height="20" rx="3" fill="#222"/></svg>
  </span></div><h3>Secured Finance</h3></div>
  <div class="feature" style="left:460px"><div class="ring"><span>
    <svg width="28" height="40" viewBox="0 0 28 40"><path d="M14 39C6 26 1 20 1 13a13 13 0 0 1 26 0c0 7-5 13-13 26z" fill="#222"/><circle cx="14" cy="13" r="5" fill="#fff"/></svg>
  </span></div><h3>Real Time Tracking</h3></div>
  <div class="feature" style="left:664px"><div class="ring"><span>
    <svg width="44" height="40" viewBox="0 0 44 40"><g fill="#222"><circle cx="16" cy="22" r="10"/><circle cx="33" cy="10" r="6"/><circle cx="34" cy="31" r="6"/></g><g fill="#fff"><circle cx="16" cy="22" r="4"/><circle cx="33" cy="10" r="2.3"/><circle cx="34" cy="31" r="2.3"/></g><g stroke="#222" stroke-width="4"><line x1="16" y1="9" x2="16" y2="35"/><line x1="3" y1="22" x2="29" y2="22"/><line x1="7" y1="13" x2="25" y2="31"/><line x1="25" y1="13" x2="7" y2="31"/><line x1="33" y1="2" x2="33" y2="18"/><line x1="25" y1="10" x2="41" y2="10"/><line x1="34" y1="23" x2="34" y2="39"/><line x1="26" y1="31" x2="42" y2="31"/></g></svg>
  </span></div><h3>Systematic Approach</h3></div>
</section>

<div class="divider"></div>

<section class="welcome">
  <h2>WELCOME TO<br>KELP ASSET MANAGEMENT</h2>
  <p>We have developed and licenced an innovative platform to provide financial institutions whom provide secured Asset finance loans to consumer and commercial clients, allowing for real time tracking and management of defaulted accounts pending repossession. The KELP Asset Management platform is a total recoveries solution through the cycle, from the moment the lender has to recover the vehicle (due to default/ non-payment) to the disposal of the vehicle (via sale at Motor Auctions or by selling &nbsp;to a Car dealership network).</p>
  <div class="btn">READ MORE</div>
  <div class="screen" role="img" aria-label="Desktop monitor showing the KELP platform voluntary surrender form"></div>
</section>

<footer class="footer">
  <div class="brand">KELP</div>
  <div class="col links" style="left:282px">
    <h4>QUICK LINKS</h4>
    <ul><li>About us</li><li>FAQ</li><li>Sitemap</li><li>Terms &amp; Conditions</li><li>Privacy Policy</li><li>Contact Us</li></ul>
  </div>
  <div class="col news" style="left:408px">
    <h4>NEWSLETTER SUBSCRIPTION</h4>
    <p>Register your Email Address to get Information about us</p>
    <div class="field">Enter Email</div>
    <div class="sub">SUBSCRIBE</div>
  </div>
  <div class="col contact" style="left:658px">
    <h4>CONTACT US</h4>
    <ul>
      <li><svg width="9" height="12" viewBox="0 0 9 12"><path d="M4.5 12C1.5 7.5 0 6 0 4.5a4.5 4.5 0 0 1 9 0C9 6 7.5 7.5 4.5 12z" fill="#fff"/><circle cx="4.5" cy="4.5" r="1.6" fill="#1f1f1f"/></svg><span>Unit 4/22 Marlow Lane<br>&nbsp;Harbour Point, Vic, 3190 Australia</span></li>
      <li><svg width="11" height="11" viewBox="0 0 11 11"><path d="M2 0l2 2.5-1.2 1.4a7 7 0 0 0 4.3 4.3L8.5 7 11 9l-1.5 2C4.5 11 0 6.5 0 1.5z" fill="#fff"/></svg><span>1 800 555 0142</span></li>
      <li><svg width="12" height="11" viewBox="0 0 12 11"><rect x="0" y="3" width="12" height="8" rx="1" fill="#fff"/><rect x="3" y="0" width="6" height="4" fill="#fff"/><rect x="3" y="5" width="6" height="1.2" fill="#1f1f1f"/><rect x="3" y="7.5" width="6" height="1.2" fill="#1f1f1f"/></svg><span>1 800 555 0187</span></li>
      <li><svg width="13" height="10" viewBox="0 0 13 10"><rect width="13" height="10" fill="#fff"/><polyline points="0,0 6.5,5.5 13,0" fill="none" stroke="#1f1f1f" stroke-width="1.3"/></svg><span>hello@kelpassetmanagement.com</span></li>
    </ul>
  </div>
  <div class="bottom-rule"></div>
  <p class="copy">Copyrights © 2018, KELP Asset Management.. All rights reserved.</p>
  <div class="social"><span></span><span></span><span></span><span></span></div>
</footer>
</body>
</html>
```